Start up Events company needs a business card design

We are a brand new start up events company that need an impressively designed business card to make the best first impression with our future clients.

Description on company:
- start-up company
- in the events management industry
- selling flagship children related event
- our future clients will mostly be vendors in the alternative education industry. dance schools, music schools, sports camp facilitators, academic establishments
- our target market are kids, parents of kids, mass market

What we need in the business card:
- we currently have a rough design that I have uploaded. we need to brush it up. make it look more professional, more vibrant but keep the meaning of the company which is called "Plum & Ladder"
- a reason for the "Plum & Ladder" concept is because we will be starting off with a flagship event & be branching out into all other related businesses relating to our core highlight which is kids & alternative education.
- this is a tentative logo we have selected - which is a girl on a swing. to represent momentum as a start up company and related to children
- if you have a better logo alternative, please do suggest it to us
- we need more colours, vibrancy yet it has to be sleek and professional.

As we are a start-up company, our budget is tight. If you have a good idea / concept, do take on this project overlooking the tight budget.
If you require any additional information, do feel free to drop us messages!

Thank you designers!

```html
<!DOCTYPE html>
<html lang="en">
<head>
<meta charset="utf-8">
<title>Plum &amp; Ladder — Business Card</title>
<link rel="stylesheet" href="https://fonts.googleapis.com/css2?family=Orbitron:wght@400;500&display=swap">
<style>
  :root {
    --backdrop: #8c8f92;
    --card: #ffffff;
    --card-shade: #f1f2f3;
    --ink: #2a2a2a;
    --muted: #6a6d70;
    --accent: #2f8fd8;
    --bar-dark: #111111;
    --bar-light: #b9bbbd;
  }
  * { box-sizing: border-box; margin: 0; padding: 0; }
  html, body { width: 1200px; height: 894px; overflow: hidden; }
  body {
    background: var(--backdrop);
    font-family: "Orbitron", sans-serif;
    color: var(--ink);
    display: flex;
    align-items: center;
    justify-content: center;
    gap: 40px;
  }
  .card {
    position: relative;
    width: 540px;
    height: 309px;
    background: linear-gradient(135deg, var(--card) 0%, var(--card-shade) 100%);
    box-shadow: 0 10px 24px rgba(0,0,0,0.25);
  }

  /* Brand mark (name set as text) */
  .brand { display: flex; align-items: center; gap: 10px; }
  .brand-dot { width: 14px; height: 14px; border-radius: 50%; background: var(--ink); }
  .brand-name { font-size: 15px; font-weight: 500; letter-spacing: 2px; text-transform: uppercase; color: var(--ink); }

  /* Contact side */
  .card-contact .brand { position: absolute; left: 36px; top: 40px; }
  .person { position: absolute; left: 92px; top: 118px; }
  .person-name { font-size: 19px; font-weight: 400; letter-spacing: 1.5px; text-transform: uppercase; }
  .person-role { margin-top: 4px; font-size: 11px; letter-spacing: 1.5px; text-transform: uppercase; color: var(--muted); }

  .details { position: absolute; top: 188px; display: flex; flex-direction: column; gap: 9px; font-size: 11px; letter-spacing: 0.8px; }
  .details-left { left: 40px; }
  .details-right { left: 316px; }
  .detail { display: flex; align-items: flex-start; gap: 8px; line-height: 1.35; }
  .detail svg { flex: none; width: 12px; height: 12px; fill: var(--accent); margin-top: 1px; }

  .bar-dark { position: absolute; left: 36px; top: 270px; width: 270px; height: 9px; background: var(--bar-dark); }
  .bar-light { position: absolute; left: 306px; top: 272px; width: 200px; height: 6px; background: var(--bar-light); }

  /* Logo side */
  .card-logo { display: flex; align-items: center; justify-content: center; }
  .logo-stack { display: flex; flex-direction: column; align-items: flex-start; gap: 6px; }
  .logo-stack .brand-name { font-size: 20px; }
  .tagline { font-size: 9px; letter-spacing: 1px; color: var(--muted); padding-left: 24px; }
</style>
</head>
<body>

  <section class="card card-contact">
    <div class="brand">
      <span class="brand-dot"></span>
      <span class="brand-name">Plum &amp; Ladder</span>
    </div>

    <div class="person">
      <p class="person-name">Daniel Marsh</p>
      <p class="person-role">General Manager</p>
    </div>

    <div class="details details-left">
      <p class="detail">
        <svg viewBox="0 0 12 12"><path d="M6 0a4 4 0 0 0-4 4c0 3 4 8 4 8s4-5 4-8a4 4 0 0 0-4-4zm0 5.5A1.5 1.5 0 1 1 6 2.5a1.5 1.5 0 0 1 0 3z"/></svg>
        <span>27 Orchard Row<br>Linden Park</span>
      </p>
      <p class="detail">
        <svg viewBox="0 0 12 12"><path d="M6 0a6 6 0 1 0 0 12A6 6 0 0 0 6 0zm4.9 5.4H8.6A9 9 0 0 0 7.7 1.3a5 5 0 0 1 3.2 4.1zM6 1.1c.7.9 1.3 2.5 1.4 4.3H4.6C4.7 3.6 5.3 2 6 1.1zM4.3 1.3a9 9 0 0 0-.9 4.1H1.1a5 5 0 0 1 3.2-4.1zM1.1 6.6h2.3a9 9 0 0 0 .9 4.1 5 5 0 0 1-3.2-4.1zM6 10.9c-.7-.9-1.3-2.5-1.4-4.3h2.8C7.3 8.4 6.7 10 6 10.9zm1.7-.2a9 9 0 0 0 .9-4.1h2.3a5 5 0 0 1-3.2 4.1z"/></svg>
        <span>www.plumandladder.co</span>
      </p>
    </div>

    <div class="details details-right">
      <p class="detail">
        <svg viewBox="0 0 12 12"><path d="M2.4 0l2 2.6-1 1.6a7 7 0 0 0 4.4 4.4l1.6-1L12 9.6 10.4 12C4.7 11.6.4 7.3 0 1.6z"/></svg>
        <span>014 555 2380</span>
      </p>
      <p class="detail">
        <svg viewBox="0 0 12 12"><path d="M3 0h6a1 1 0 0 1 1 1v10a1 1 0 0 1-1 1H3a1 1 0 0 1-1-1V1a1 1 0 0 1 1-1zm0 1.5v8h6v-8zM6 10.2a.6.6 0 1 0 0 1.2.6.6 0 0 0 0-1.2z"/></svg>
        <span>014 555 2381</span>
      </p>
      <p class="detail">
        <svg viewBox="0 0 12 12"><path d="M0 2h12v8H0zm1 1v.4l5 3.2 5-3.2V3zm0 1.6V9h10V4.6L6 7.8z"/></svg>
        <span>hello@plumandladder.co</span>
      </p>
    </div>

    <div class="bar-dark"></div>
    <div class="bar-light"></div>
  </section>

  <section class="card card-logo">
    <div class="logo-stack">
      <div class="brand">
        <span class="brand-dot"></span>
        <span class="brand-name">Plum &amp; Ladder</span>
      </div>
      <p class="tagline">Inspiring young learners</p>
    </div>
  </section>

</body>
</html>
```